New Business Card Design Project

Want a simple but attention grabbing business card. Back Side having mainly our logo and basic info-the front side a typical business card.

Contact Information for Business Card

Hearth & Tile Interiors
218 NW Larkspur Rd. Suite 207
Ankeny, Iowa 50021

phone- 515.482.7093

website is -htidesigns.com

```html
<!DOCTYPE html>
<html lang="en">
<head>
<meta charset="utf-8">
<title>Hearth &amp; Tile Interiors – Business Card</title>
<link href="https://fonts.googleapis.com/css2?family=Open+Sans:wght@400;700&display=swap" rel="stylesheet">
<style>
  :root {
    --page-bg: #e6e6e6;
    --card-white: #ffffff;
    --stone-light: #a9a9a9;
    --stone-mid: #9a9a9a;
    --stone-dark: #8c8c8c;
    --ink-grey: #7a7a7a;
    --mark-grey: #d2d2d2;
    --front-text: #ffffff;
  }
  * { margin: 0; padding: 0; box-sizing: border-box; }
  html, body {
    width: 1200px;
    height: 1144px;
    overflow: hidden;
    background: var(--page-bg);
    font-family: "Open Sans", Arial, sans-serif;
  }
  .canvas {
    position: relative;
    width: 1200px;
    height: 1144px;
  }
  .card {
    position: absolute;
    left: 295px;
    width: 610px;
    height: 348px;
  }
  .card--front { top: 194px; }
  .card--back {
    top: 591px;
    background: var(--card-white);
  }
  .stone-surface {
    position: absolute;
    inset: 0;
    background:
      radial-gradient(ellipse at 80% 30%, var(--stone-dark) 0%, transparent 55%),
      radial-gradient(ellipse at 15% 80%, var(--stone-mid) 0%, transparent 60%),
      linear-gradient(135deg, var(--stone-light), var(--stone-mid));
  }
  .front-brand {
    position: absolute;
    left: 0;
    right: 0;
    top: 158px;
    text-align: center;
    color: var(--front-text);
    font-weight: 700;
    font-size: 34px;
    letter-spacing: 1px;
    text-transform: uppercase;
  }
  .contact {
    position: absolute;
    left: 215px;
    top: 94px;
    color: var(--ink-grey);
    font-size: 17px;
    line-height: 1.2;
  }
  .contact__name { margin-bottom: 18px; }
  .contact__name strong { font-weight: 700; }
  .contact__address { margin-bottom: 18px; }
  .corner-brand {
    position: absolute;
    right: 26px;
    bottom: 26px;
    color: var(--mark-grey);
    font-weight: 700;
    font-size: 15px;
    text-transform: uppercase;
    letter-spacing: 0.5px;
  }
</style>
</head>
<body>
<main class="canvas">
  <section class="card card--front">
    <div class="stone-surface" role="img" aria-label="Grey polished concrete texture background"></div>
    <h1 class="front-brand">Hearth &amp; Tile Interiors</h1>
  </section>

  <section class="card card--back">
    <div class="contact">
      <p class="contact__name">DANA <strong>WHITFIELD</strong></p>
      <p class="contact__address">218 NW Larkspur Rd.<br>Suite 207<br>Ankeny, IA 50021</p>
      <p class="contact__phone">515.482.7093</p>
      <p class="contact__email">dana@htidesigns.com</p>
    </div>
    <p class="corner-brand">Hearth &amp; Tile Interiors</p>
  </section>
</main>
</body>
</html>
```